A label for my commercially sold local honey. This is a LABEL not a logo

3 inches high
2 inches wide

Target Market(s)

Customers who like "local" honey

Logo Text

Wildflower Honey -- 100% Pure & Unfiltered -- Florida

Logo styles of interest
Wordmark Logo
Requirements
Must have
• Wildflower Honey -- 100% Pure & Unfiltered -- Florida

Florida should be dominant

3 inches high / 2 inches wide

```html
<!DOCTYPE html>
<html lang="en">
<head>
<meta charset="UTF-8">
<title>Wildflower Honey Label</title>
<link rel="stylesheet" href="https://fonts.googleapis.com/css2?family=Roboto:wght@400;500;700;900&display=swap">
<style>
  :root {
    --canvas: #ffffff;
    --label-cream-light: #f6ead9;
    --label-cream-dark: #ecdcc4;
    --ink: #1b1b1b;
    --frame: #3a3a3a;
    --tag-light: #efefef;
    --tag-dark: #c8c8c8;
  }
  html, body {
    margin: 0;
    padding: 0;
    overflow: hidden;
    background: var(--canvas);
  }
  .canvas {
    position: relative;
    width: 1200px;
    height: 1200px;
    background: var(--canvas);
    overflow: hidden;
    font-family: "Roboto", sans-serif;
    color: var(--ink);
  }

  /* Front label */
  .front-label {
    position: absolute;
    left: 140px;
    top: 190px;
    width: 480px;
    height: 820px;
    background: linear-gradient(90deg, var(--label-cream-dark), var(--label-cream-light) 30%, var(--label-cream-light) 70%, var(--label-cream-dark));
  }
  .front-label .inner-frame {
    position: absolute;
    inset: 12px;
    border: 1.5px solid var(--frame);
  }
  .front-label .top-band {
    position: absolute;
    left: 90px;
    top: 0;
    width: 300px;
    height: 58px;
  }
  .front-label .bottom-band {
    position: absolute;
    left: 90px;
    bottom: 22px;
    width: 300px;
    height: 78px;
  }
  .brand-name {
    position: absolute;
    left: 0;
    right: 0;
    text-align: center;
    font-weight: 500;
    color: var(--ink);
    letter-spacing: 0.04em;
    line-height: 1.15;
  }
  .front-label .brand-name {
    top: 290px;
    font-size: 46px;
  }
  .front-label .divider {
    position: absolute;
    left: -6px;
    right: -6px;
    top: 480px;
    height: 2px;
    background: var(--ink);
  }
  .product-name {
    position: absolute;
    left: 0;
    right: 0;
    top: 490px;
    margin: 0;
    text-align: center;
    font-size: 44px;
    font-weight: 400;
    line-height: 1.2;
  }
  .product-claim {
    position: absolute;
    left: 0;
    right: 0;
    top: 550px;
    margin: 0;
    text-align: center;
    font-size: 19px;
    font-weight: 700;
    line-height: 1.3;
  }
  .product-origin {
    position: absolute;
    left: 0;
    right: 0;
    top: 580px;
    margin: 0;
    text-align: center;
    font-size: 72px;
    font-weight: 900;
    letter-spacing: 0.06em;
    text-transform: uppercase;
    line-height: 1.1;
  }

  /* Hexagonal hang tag */
  .hang-tag {
    position: absolute;
    left: 660px;
    top: 410px;
    width: 440px;
    height: 380px;
  }
  .hang-tag svg {
    position: absolute;
    inset: 0;
  }
  .hang-tag .brand-name {
    top: 140px;
    font-size: 36px;
  }
</style>
</head>
<body>
<main class="canvas">

  <section class="front-label">
    <div class="inner-frame"></div>
    <svg class="top-band" viewBox="0 0 300 58" aria-hidden="true">
      <polygon points="0,0 300,0 300,36 150,58 0,36" fill="#1b1b1b"/>
    </svg>
    <div class="brand-name">Palm Hollow<br>Mkt</div>
    <div class="divider"></div>
    <h1 class="product-name">Wildflower Honey</h1>
    <p class="product-claim">100% Pure &amp; Unfiltered --</p>
    <p class="product-origin">Florida</p>
    <svg class="bottom-band" viewBox="0 0 300 78" aria-hidden="true">
      <polygon points="0,22 150,0 300,22 300,78 0,78" fill="#1b1b1b"/>
    </svg>
  </section>

  <section class="hang-tag">
    <svg viewBox="0 0 440 380" aria-hidden="true">
      <defs>
        <linearGradient id="tag-fill" x1="0" x2="1" y1="0" y2="0">
          <stop offset="0" stop-color="#efefef"/>
          <stop offset="1" stop-color="#c8c8c8"/>
        </linearGradient>
        <clipPath id="tag-shape">
          <polygon points="0,190 110,0 330,0 440,190 330,380 110,380"/>
        </clipPath>
      </defs>
      <polygon points="0,190 110,0 330,0 440,190 330,380 110,380" fill="url(#tag-fill)"/>
      <polygon points="22,190 121,18 319,18 418,190 319,362 121,362" fill="none" stroke="#2a2a2a" stroke-width="1.5"/>
      <g clip-path="url(#tag-shape)">
        <polygon points="0,318 220,300 440,318 440,380 0,380" fill="#1b1b1b"/>
      </g>
      <polygon points="150,0 290,0 290,48 220,66 150,48" fill="#1b1b1b"/>
      <circle cx="220" cy="30" r="11" fill="#ffffff"/>
    </svg>
    <div class="brand-name">Palm Hollow<br>Mkt</div>
  </section>

</main>
</body>
</html>
```